Harborline Consultancy & Training Organization Web Site Design

Help!

We have started designing and building a Web site to promote and sell training services to HR managers. But we are not very good designers. In fact, we stink.

We have a logo.

We have most of the content (more or less) and the site architecture. But we have put together a pretty lousy look and feel.

Take a look: http://harborlinewise.example/pqvtlnwiseindex.html

What we'd like is a Web 3.0 type design - clean, simple, modern looking. Some sites we admire:

tilbrook.org
velquora.com
skorvane.com
brindlewords.com
ormak.com

We have access to stock photography, some of which we've used on the site we've built so far. You can use those and others. But keep it simple.

Target Market(s)

Professional HR managers in larger companies

Industry/Entity Type

Requirements
Must have
• Use our logo and a color scheme based off of it. Logo file uploaded.

Need to see home page and examples of secondary pages, based on site currently online.

```html
<!DOCTYPE html>
<html lang="en">
<head>
<meta charset="utf-8">
<title>Harborline — Generational Tools &amp; Training for HR Professionals</title>
<link rel="stylesheet" href="https://fonts.googleapis.com/css2?family=PT+Sans:wght@400;700&display=swap">
<style>
:root{
  --ink:#2c2c2c;
  --muted:#555;
  --topbar:#2a2a2a;
  --brand-blue:#1d3f94;
  --brand-blue-dark:#15307a;
  --link:#1f4fa8;
  --tagline:#2e62a6;
  --band:#e6edf2;
  --rule:#cfdbe0;
  --accent-orange:#f08a24;
  --gray-logo:#8a8a8a;
}
*{margin:0;padding:0;box-sizing:border-box}
html,body{width:1200px;height:857px;overflow:hidden;background:#fff}
body{font-family:"PT Sans",sans-serif;color:var(--ink);position:relative}
a{text-decoration:none;color:inherit}

.topbar{position:absolute;left:0;top:0;width:1200px;height:30px;background:var(--topbar)}
.topbar-nav{position:absolute;left:686px;top:8px;display:flex;gap:23px;font-size:11.5px;color:#eee}
.social{position:absolute;top:6px;font-size:13px;font-weight:700;color:#fff}
.social.friend{left:872px}
.social.chirp{left:952px}

.band{position:absolute;left:0;top:30px;width:1200px;height:465px;
  background:linear-gradient(180deg,#f3f6f8 0%,var(--band) 100%)}

.brand{position:absolute;left:189px;top:38px;display:flex;align-items:center;gap:9px}
.brand-mark{width:18px;height:18px;background:var(--brand-blue);border-radius:50%}
.brand-name{font-size:22px;color:#333}
.tagline{position:absolute;right:195px;top:55px;font-size:17px;color:var(--tagline)}

.hero{position:absolute;left:185px;top:105px;width:823px;height:275px;border-radius:3px;
  background:linear-gradient(180deg,#b9dcef 0%,#d9edf7 55%,#a9b4bb 100%);
  box-shadow:0 1px 4px rgba(0,0,0,.25)}
.side-menu{position:absolute;left:197px;top:91px;width:126px;list-style:none;
  background:linear-gradient(180deg,#2a4fa8,var(--brand-blue-dark));border-radius:2px 2px 0 0;
  box-shadow:0 1px 3px rgba(0,0,0,.3)}
.side-menu li{height:21.4px;line-height:21.4px;padding-left:12px;font-size:12.5px;color:#fff;
  border-bottom:1px solid rgba(255,255,255,.18)}
.side-menu li:last-child{border-bottom:none}

.promo{position:absolute;top:411px;width:257px;height:63px;
  background:linear-gradient(180deg,#fff,#e6e6e6);border-bottom:3px solid var(--brand-blue);
  box-shadow:0 1px 3px rgba(0,0,0,.2)}
.promo-photo{position:absolute;left:0;top:-19px;width:103px;height:79px;
  background:linear-gradient(180deg,#cfcfcf,#6f6f6f)}
.promo-title{position:absolute;right:34px;top:19px;font-size:16.5px;color:#333}
.promo svg{position:absolute;right:10px;top:14px}

.intro{position:absolute;left:188px;top:511px;font-size:17px;color:#333}
.more{position:absolute;left:879px;top:513px;font-size:15px;color:var(--link);display:flex;align-items:center;gap:8px}

.feature{position:absolute;top:560px;width:180px}
.feature-icon{position:absolute;left:0;top:0}
.feature-title{position:absolute;left:48px;top:9px;font-size:17px;color:#333}
.feature-text{position:absolute;left:50px;top:38px;font-size:10.5px;line-height:14px;color:#444;width:110px}

.rule{position:absolute;left:193px;width:823px;height:1px;background:var(--rule)}

.clients{position:absolute;left:197px;top:692px;display:flex;align-items:center;gap:10px}
.clients-label{font-size:16px;line-height:15px;color:#333}
.client{position:absolute;top:696px;font-size:20px;color:var(--gray-logo)}

.footer-copy{position:absolute;left:191px;top:772px;font-size:10.5px;color:#333}
.footer-nav{position:absolute;left:456px;top:771px;display:flex;gap:16px;font-size:11px;color:var(--link)}
</style>
</head>
<body>

<header class="topbar">
  <nav class="topbar-nav"><a href="#">Home</a><a href="#">About Us</a><a href="#">Contact</a></nav>
  <a class="social friend" href="#">Friendloop</a>
  <a class="social chirp" href="#">Chirpline</a>
</header>

<div class="band"></div>

<div class="brand"><span class="brand-mark"></span><span class="brand-name">Harborline</span></div>
<p class="tagline">Generational Tools &amp; Training for HR Professionals</p>

<div class="hero" role="img" aria-label="Four smiling business professionals of different generations standing against a light blue sky"></div>
<ul class="side-menu">
  <li>Home</li><li>Gen 101</li><li>Gen Gaps</li><li>Strategies</li><li>Resources</li>
  <li>Training</li><li>Tools</li><li>Discuss</li><li>About</li><li>Contact</li>
</ul>

<a class="promo" href="#" style="left:198px">
  <div class="promo-photo" role="img" aria-label="Two men of different ages in business dress"></div>
  <span class="promo-title">Generations 101</span>
  <svg width="14" height="32" viewBox="0 0 14 32"><path d="M1 1 L13 16 L1 31" fill="none" stroke="#f08a24" stroke-width="1.5"/></svg>
</a>
<a class="promo" href="#" style="left:471px">
  <div class="promo-photo" role="img" aria-label="Two women of different ages smiling"></div>
  <span class="promo-title">Generation Gaps</span>
  <svg width="14" height="32" viewBox="0 0 14 32"><path d="M1 1 L13 16 L1 31" fill="none" stroke="#e0282c" stroke-width="1.5"/></svg>
</a>
<a class="promo" href="#" style="left:747px">
  <div class="promo-photo" role="img" aria-label="Two businessmen standing together"></div>
  <span class="promo-title">Gen Strategies</span>
  <svg width="14" height="32" viewBox="0 0 14 32"><path d="M1 1 L13 16 L1 31" fill="none" stroke="#3aa04a" stroke-width="1.5"/></svg>
</a>

<p class="intro">Harborline is committed to providing HR professionals with training that matters.</p>
<a class="more" href="#">tell me more
  <svg width="20" height="10" viewBox="0 0 20 10"><path d="M0 5 H18 M13 1 L18 5 L13 9" fill="none" stroke="#f08a24" stroke-width="1.4"/></svg>
</a>

<section class="feature" style="left:200px">
  <svg class="feature-icon" width="40" height="40" viewBox="0 0 40 40"><circle cx="20" cy="18" r="17" fill="#2a5fc8"/><rect x="14" y="10" width="11" height="15" rx="1" fill="none" stroke="#fff" stroke-width="2"/><rect x="17" y="13" width="9" height="13" rx="1" fill="#2a5fc8" stroke="#fff" stroke-width="2"/></svg>
  <h3 class="feature-title" style="font-weight:400">Resources</h3>
  <p class="feature-text">What makes our trainings so much better than the rest.</p>
</section>
<section class="feature" style="left:413px">
  <svg class="feature-icon" width="40" height="40" viewBox="0 0 40 40"><circle cx="20" cy="18" r="17" fill="#2a5fc8"/><path d="M23 7 L13 20 H19 L16 30 L27 16 H21 Z" fill="#fff"/></svg>
  <h3 class="feature-title" style="font-weight:400">Training</h3>
  <p class="feature-text">What makes our trainings so much better than the rest.</p>
</section>
<section class="feature" style="left:615px">
  <svg class="feature-icon" width="40" height="40" viewBox="0 0 40 40"><circle cx="20" cy="18" r="17" fill="#2a5fc8"/><path d="M12 26 L26 11 M12 11 L26 26" stroke="#fff" stroke-width="3" stroke-linecap="round"/></svg>
  <h3 class="feature-title" style="font-weight:400">Tools</h3>
  <p class="feature-text">What makes our trainings so much better than the rest.</p>
</section>
<section class="feature" style="left:823px">
  <svg class="feature-icon" width="40" height="40" viewBox="0 0 40 40"><circle cx="20" cy="18" r="17" fill="#2a5fc8"/><ellipse cx="20" cy="17" rx="10" ry="7" fill="#fff"/><path d="M13 21 L11 27 L18 23 Z" fill="#fff"/></svg>
  <h3 class="feature-title" style="font-weight:400">Discuss</h3>
  <p class="feature-text">What makes our trainings so much better than the rest.</p>
</section>

<div class="rule" style="top:670px"></div>

<div class="clients">
  <svg width="12" height="20" viewBox="0 0 12 20"><path d="M2 2 H10 L7 8 L10 12 H6 V19 L5 12 H1 L4 8 Z" fill="#f08a24"/></svg>
  <span class="clients-label">Companies<br>We Work With</span>
</div>
<span class="client" style="left:365px;font-weight:700">Cocoabrook</span>
<span class="client" style="left:494px">Steadfast Mutual</span>
<span class="client" style="left:690px">Searchwell</span>
<span class="client" style="left:833px">Carroway &amp; Finch</span>

<div class="rule" style="top:746px"></div>

<p class="footer-copy">Copyright 2011, QLT Research</p>
<nav class="footer-nav">
  <a href="#">Home</a><a href="#">Gen 101</a><a href="#">Gen Gaps</a><a href="#">Strategies</a><a href="#">Resources</a>
  <a href="#">Training</a><a href="#">Tools</a><a href="#">Discuss</a><a href="#">About</a><a href="#">Contact</a>
</nav>

</body>
</html>
```